Core Values Poster for Healthcare company

Trying to Create a core values poster for my company. Healthcare Company - We have Neurosurgery, Pain Management, Physical Therapy, Occupational Therapy, Rehab, Imaging, and psychology so far and we are growing fast.

Core Values would Include - (Execution), (Loyalty), (Innovation), (Synergy), (Growth-Oriented), (Ethics & Integrity), (Love), and (Energy)

Please incorporate the Company Logo which is on the website and I have included it in my uploads. As long as the logo stays blue it does not need a gradient effect.

I like the posters made for this contest : https://quillvane.com.au/poster-design/contests/make-team-principles-wallchart-815327

This picture should be memorable so people know our Core Values

Target Market(s)

Staff in the company

Colors

Designer to choose colors to be used in the design.

Requirements
Must have
• Logo
Nice to have
• Pictures for each core value

```html
<!DOCTYPE html>
<html lang="en">
<head>
<meta charset="utf-8">
<title>Lumenpath Core Values Poster</title>
<link rel="stylesheet" href="https://fonts.googleapis.com/css2?family=Cinzel:wght@500;700&family=Patua+One&display=swap">
<style>
  :root {
    --paper-light: #ffffff;
    --paper-edge: #c9cad2;
    --brand-blue: #1c9ad6;
    --banner-red: #e8202a;
    --execution: #23a560;
    --innovation: #f39a1e;
    --synergy: #6a2c91;
    --love: #e3252b;
    --love-soft: #f0474c;
    --loyalty: #e0168a;
    --loyalty-soft: #ec4fa8;
    --growth: #6fb52c;
    --ethics: #8c1a5a;
    --stem-dark: #3a3a3a;
    --white: #ffffff;
  }
  html, body {
    margin: 0;
    width: 1200px;
    height: 1148px;
    overflow: hidden;
  }
  .poster {
    position: relative;
    width: 1200px;
    height: 1148px;
    background: radial-gradient(ellipse at 45% 55%, var(--paper-light) 0%, #eeeef2 45%, var(--paper-edge) 100%);
  }
  .brand {
    position: absolute;
    top: 30px;
    left: 0;
    width: 1200px;
    display: flex;
    justify-content: center;
    align-items: center;
    gap: 22px;
  }
  .brand-square {
    width: 80px;
    height: 80px;
    background: var(--brand-blue);
  }
  .brand-name {
    font-family: "Cinzel", serif;
    font-weight: 500;
    font-size: 88px;
    line-height: 1;
    color: var(--brand-blue);
    letter-spacing: 2px;
  }
  .values-banner {
    position: absolute;
    top: 164px;
    left: 410px;
    width: 380px;
    height: 80px;
    border-radius: 8px;
    background: var(--banner-red);
    color: var(--white);
    font-family: "Cinzel", serif;
    font-weight: 700;
    font-size: 38px;
    display: flex;
    align-items: center;
    justify-content: center;
    box-shadow: 0 3px 6px rgba(0,0,0,.25);
  }
  .values-banner::before, .values-banner::after {
    content: "";
    position: absolute;
    width: 8px; height: 8px;
    border-radius: 50%;
    background: var(--white);
    top: 12px; left: 12px;
    box-shadow: 0 48px 0 var(--white);
  }
  .values-banner::after { left: auto; right: 12px; }
  .diagram { position: absolute; top: 0; left: 0; }
  .label { font-family: "Patua One", serif; font-size: 38px; }
  .label-execution { fill: var(--execution); }
  .label-innovation { fill: var(--innovation); }
  .label-synergy { fill: var(--synergy); }
  .label-love { fill: var(--love); }
  .label-loyalty { fill: var(--loyalty); }
  .label-growth { fill: var(--growth); }
  .label-ethics { fill: var(--ethics); }
  .stem { fill: none; stroke-width: 5; stroke-linejoin: round; }
  .icon-line { fill: none; stroke: var(--white); stroke-linecap: round; stroke-linejoin: round; }
</style>
</head>
<body>
<main class="poster">
  <header class="brand">
    <div class="brand-square"></div>
    <div class="brand-name">LUMENPATH</div>
  </header>
  <div class="values-banner">CORE VALUES</div>

  <svg class="diagram" width="1200" height="1148" viewBox="0 0 1200 1148">
    <defs>
      <filter id="lift" x="-30%" y="-30%" width="160%" height="160%">
        <feDropShadow dx="3" dy="5" stdDeviation="4" flood-opacity=".3"/>
      </filter>
      <linearGradient id="careFill" x1="0" y1="0" x2="0" y2="1">
        <stop offset="0" stop-color="var(--love-soft)"/>
        <stop offset="1" stop-color="var(--love)"/>
      </linearGradient>
    </defs>

    <g class="stems">
      <path class="stem" stroke="var(--stem-dark)" d="M540 690 H600 Q605 690 605 695 V910"/>
      <path class="stem" stroke="var(--synergy)" d="M440 586 H610 Q615 586 615 591 V910"/>
      <path class="stem" stroke="var(--innovation)" d="M325 490 H620 Q625 490 625 495 V910"/>
      <path class="stem" stroke="var(--execution)" d="M600 440 Q600 450 612 460 Q635 480 635 500 V910"/>
      <path class="stem" stroke="var(--loyalty)" d="M845 478 H650 Q645 478 645 483 V910"/>
      <path class="stem" stroke="var(--growth)" d="M760 572 H662 Q657 572 657 577 V910"/>
      <path class="stem" stroke="var(--ethics)" d="M690 680 H673 Q668 680 668 685 V910"/>
    </g>

    <g class="value-execution">
      <text class="label label-execution" x="600" y="300" text-anchor="middle">Execution</text>
      <circle cx="600" cy="378" r="72" fill="var(--execution)" filter="url(#lift)"/>
      <g class="icon-gears">
        <circle cx="588" cy="392" r="20" fill="var(--white)"/>
        <circle cx="588" cy="392" r="24" fill="none" stroke="var(--white)" stroke-width="8" stroke-dasharray="6 6.6"/>
        <circle cx="588" cy="392" r="9" fill="var(--execution)"/>
        <circle cx="624" cy="356" r="13" fill="var(--white)"/>
        <circle cx="624" cy="356" r="17" fill="none" stroke="var(--white)" stroke-width="6" stroke-dasharray="5 5.7"/>
        <circle cx="624" cy="356" r="6" fill="var(--execution)"/>
      </g>
    </g>

    <g class="value-innovation">
      <text class="label label-innovation" x="280" y="410" text-anchor="middle">Innovation</text>
      <circle cx="259" cy="488" r="72" fill="var(--innovation)" filter="url(#lift)"/>
      <g class="icon-bulb">
        <circle cx="259" cy="476" r="27" fill="var(--white)"/>
        <path d="M245 494 H273 L270 512 H248Z" fill="var(--white)"/>
        <rect x="248" y="516" width="22" height="5" rx="2" fill="var(--white)"/>
        <rect x="251" y="524" width="16" height="5" rx="2" fill="var(--white)"/>
        <circle cx="259" cy="476" r="12" fill="none" stroke="var(--innovation)" stroke-width="5" stroke-dasharray="4 4.4"/>
        <circle cx="259" cy="476" r="5" fill="var(--innovation)"/>
      </g>
    </g>

    <g class="value-synergy">
      <text class="label label-synergy" x="190" y="645" text-anchor="middle">Synergy</text>
      <circle cx="375" cy="584" r="72" fill="var(--synergy)" filter="url(#lift)"/>
      <g class="icon-links">
        <circle cx="375" cy="584" r="30" class="icon-line" stroke-width="3"/>
        <circle cx="375" cy="554" r="8" fill="var(--synergy)" class="icon-line" stroke-width="5"/>
        <circle cx="403" cy="575" r="8" fill="var(--synergy)" class="icon-line" stroke-width="5"/>
        <circle cx="393" cy="608" r="8" fill="var(--synergy)" class="icon-line" stroke-width="5"/>
        <circle cx="357" cy="608" r="8" fill="var(--synergy)" class="icon-line" stroke-width="5"/>
        <circle cx="347" cy="575" r="8" fill="var(--synergy)" class="icon-line" stroke-width="5"/>
      </g>
    </g>

    <g class="value-love">
      <text class="label label-love" x="340" y="775" text-anchor="middle">Love &amp;</text>
      <text class="label label-love" x="350" y="818" text-anchor="middle">Energy</text>
      <circle cx="476" cy="687" r="72" fill="var(--love)" filter="url(#lift)"/>
      <path fill="var(--white)" d="M476 730 C446 710 432 694 432 676 C432 662 443 652 456 652 C465 652 472 657 476 664 C480 657 487 652 496 652 C509 652 520 662 520 676 C520 694 506 710 476 730Z"/>
      <path fill="var(--love)" d="M480 660 L466 690 L477 690 L470 712 L488 682 L477 682 L484 660Z"/>
    </g>

    <g class="value-loyalty">
      <text class="label label-loyalty" x="905" y="395" text-anchor="middle">Loyalty</text>
      <circle cx="910" cy="474" r="72" fill="var(--loyalty)" filter="url(#lift)"/>
      <circle cx="910" cy="474" r="40" fill="var(--loyalty-soft)" role="img" aria-label="Loyalty pictogram: person with hand on heart"/>
    </g>

    <g class="value-growth">
      <text class="label label-growth" x="970" y="668" text-anchor="middle">Growth-</text>
      <text class="label label-growth" x="985" y="710" text-anchor="middle">Oriented</text>
      <circle cx="825" cy="570" r="72" fill="var(--growth)" filter="url(#lift)"/>
      <g fill="var(--white)">
        <rect x="790" y="590" width="11" height="20"/>
        <rect x="806" y="582" width="11" height="28"/>
        <rect x="822" y="572" width="11" height="38"/>
        <rect x="838" y="560" width="11" height="50"/>
        <rect x="854" y="546" width="11" height="64"/>
      </g>
      <path d="M792 578 Q830 568 852 530" fill="none" stroke="var(--white)" stroke-width="6"/>
      <path d="M842 526 L860 518 L860 540Z" fill="var(--white)"/>
    </g>

    <g class="value-ethics">
      <text class="label label-ethics" x="880" y="800" text-anchor="middle">Ethics &amp;</text>
      <text class="label label-ethics" x="888" y="842" text-anchor="middle">Integrity</text>
      <circle cx="752" cy="679" r="72" fill="var(--ethics)" filter="url(#lift)"/>
      <g class="icon-scale">
        <circle cx="752" cy="650" r="5" fill="var(--white)"/>
        <rect x="749" y="652" width="6" height="44" fill="var(--white)"/>
        <path d="M720 662 H784" class="icon-line" stroke-width="5"/>
        <path d="M722 663 L710 688 M722 663 L734 688 M782 663 L770 688 M782 663 L794 688" class="icon-line" stroke-width="2.5"/>
        <path d="M708 688 H736 Q722 702 708 688Z" fill="var(--white)"/>
        <path d="M768 688 H796 Q782 702 768 688Z" fill="var(--white)"/>
        <rect x="736" y="696" width="32" height="8" rx="2" fill="var(--white)"/>
        <rect x="728" y="706" width="48" height="8" rx="2" fill="var(--white)"/>
      </g>
    </g>

    <rect class="care-emblem" x="510" y="880" width="335" height="240" rx="40" fill="url(#careFill)" filter="url(#lift)" role="img" aria-label="Healthcare emblem: red heart with heartbeat line and medical cross"/>
  </svg>
</main>
</body>
</html>
```